UNIVERSITY OF CASTERBROOK SAXOPHONE SENIOR RECITAL

I need a poster design for my senior saxophone recital. The title of it is "Hollow: a Voyage across the Width of Tone". My concept is completely contrasting to the idea of a typical university recital. I'm so put off by the idea of "clap..clap..{play some music}..clap..clap..repeat". My recital is all based off of sound. The music I selected is all very modern (i.e Piet Halvermuss 'Warm Past the Final Pour' for Saxophone and Coffee Machine). I've included the Gatherly link so you can see the picture I have in the background. I like the idea of minimal black and white photography. Also, I would like the time / date / location / etc. all included on it. Let your imaginations run wild! It's art for an artist!
https://www.gatherly.example/events/413920587716230/
Target Market(s)
University Students around the University of Casterbrook and locals around the art district of South Beach, FL.
Industry/Entity Type
University

```html
<!DOCTYPE html>
<html lang="en">
<head>
<meta charset="utf-8">
<title>Hollow — Senior Saxophone Recital</title>
<link href="https://fonts.googleapis.com/css2?family=Advent+Pro:wght@200;300;500;700&family=Oswald:wght@400&display=swap" rel="stylesheet">
<style>
  :root {
    --night: #000000;
    --asphalt-dark: #2a2a2a;
    --asphalt-mid: #8d8d8d;
    --asphalt-light: #d9d9d9;
    --ink: #111111;
    --paper: #ffffff;
  }
  * { margin: 0; padding: 0; box-sizing: border-box; }
  html, body {
    width: 960px; height: 1200px; overflow: hidden;
    background: var(--night);
  }
  .poster {
    position: relative; width: 960px; height: 1200px; overflow: hidden;
    background: var(--night);
  }
  .night-road {
    position: absolute; inset: 0;
    background:
      radial-gradient(ellipse 140% 55% at 50% 100%, transparent 55%, rgba(0,0,0,0.55) 100%),
      radial-gradient(ellipse 90% 60% at 62% 82%, var(--asphalt-light) 0%, #b5b5b5 35%, var(--asphalt-mid) 62%, var(--asphalt-dark) 88%),
      var(--night);
    -webkit-mask: linear-gradient(to bottom, transparent 0, transparent 420px, #000 540px);
            mask: linear-gradient(to bottom, transparent 0, transparent 420px, #000 540px);
  }
  .title {
    position: absolute; top: 40px; left: 0; width: 100%;
    text-align: center; color: var(--paper);
    font-family: "Advent Pro", sans-serif; font-weight: 300;
    font-size: 262px; line-height: 1; letter-spacing: 0;
    transform: scaleX(0.6); transform-origin: 50% 0;
  }
  .subtitle {
    position: absolute; top: 362px; left: 0; width: 100%;
    text-align: center; color: var(--paper);
    font-family: "Oswald", sans-serif; font-weight: 400;
    font-size: 29px; letter-spacing: 1.5px;
  }
  .date { position: absolute; top: 672px; left: 0; width: 100%; text-align: center; color: var(--ink); font-family: "Advent Pro", sans-serif; }
  .date-day { font-size: 56px; font-weight: 500; line-height: 1; }
  .date-month { font-size: 62px; font-weight: 700; letter-spacing: 10px; line-height: 1.05; margin-left: 10px; }
  .date-year { font-size: 58px; font-weight: 200; letter-spacing: 38px; line-height: 1; margin-left: 38px; }
  .venue {
    position: absolute; top: 990px; left: 0; width: 100%;
    text-align: center; color: var(--ink);
    font-family: "Advent Pro", sans-serif; font-weight: 700;
    font-size: 44px; letter-spacing: 13px; line-height: 1.25;
  }
</style>
</head>
<body>
  <main class="poster">
    <div class="night-road" role="img" aria-label="Black and white night photograph of a headlight-lit empty road with a road sign at its far edge"></div>

    <h1 class="title">HOLLOW</h1>
    <p class="subtitle">A VOYAGE ACROSS THE WIDTH OF TONE</p>

    <div class="date">
      <div class="date-day">8</div>
      <div class="date-month">DECEMBER</div>
      <div class="date-year">2013</div>
    </div>

    <p class="venue">MARLOW T. KEANE<br>RECITAL HALL</p>
  </main>
</body>
</html>
```